Tovin Wine Label Design Project

We are creating a wine with a winery in New Hampshire. USA. The bottles need a label Here are some specifics
Brand name Silvara XIV (latin for Grove 14)
Wine: is a blend of Cabernet Sauvignon, Merlot and Shiraz (dominant varietal is cabernet)
Vintage 2023
All ideas from here are thoughts:
Elegant serif or calligraphic script for a sophisticated look. Perhaps Gold foil or embossed for prominence.
Background suggestions: deep Burgandy or matt black for contrast
Illustrations suggestions: Roman inspired wreath (laurel) or column or stylized roman coin.
Tagline suggestion: Timeless
All these graphic elements are just suggestions, you all are the pros. have at it and good luck

```html
<!DOCTYPE html>
<html lang="en">
<head>
<meta charset="utf-8">
<title>Silvara XIV – Wine Label</title>
<link rel="stylesheet" href="https://fonts.googleapis.com/css2?family=Cinzel:wght@500;600&family=EB+Garamond:wght@500&display=swap">
<style>
  :root {
    --backdrop: #2e2e30;
    --label-black: #0e0e0f;
    --gold: #c9a96a;
    --gold-light: #e6cf98;
    --gold-deep: #8a6c3a;
    --varietal-grey: #c9c6c0;
    --origin-grey: #a9a6a1;
    --vintage-red: #b8434b;
  }
  html, body {
    margin: 0;
    padding: 0;
    width: 1200px;
    height: 900px;
    overflow: hidden;
    background: var(--backdrop);
  }
  .canvas {
    position: relative;
    width: 1200px;
    height: 900px;
    background: var(--backdrop);
  }
  .label {
    position: absolute;
    left: 340px;
    top: 60px;
    width: 520px;
    height: 760px;
  }
  .label-shape {
    position: absolute;
    inset: 0;
  }
  .label-text {
    position: absolute;
    left: 0;
    width: 520px;
    margin: 0;
    text-align: center;
    text-transform: uppercase;
  }
  .brand-name {
    top: 390px;
    font-family: "Cinzel", serif;
    font-weight: 600;
    font-size: 44px;
    letter-spacing: 0.16em;
    color: var(--gold-light);
  }
  .varietals {
    top: 510px;
    font-family: "EB Garamond", serif;
    font-weight: 500;
    font-size: 20px;
    line-height: 1.3;
    letter-spacing: 0.16em;
    color: var(--varietal-grey);
  }
  .vintage {
    top: 600px;
    font-family: "EB Garamond", serif;
    font-weight: 500;
    font-size: 16px;
    letter-spacing: 0.2em;
    color: var(--vintage-red);
  }
  .origin {
    top: 680px;
    font-family: "EB Garamond", serif;
    font-weight: 500;
    font-size: 15px;
    letter-spacing: 0.22em;
    color: var(--origin-grey);
  }
</style>
</head>
<body>
<main class="canvas">
  <section class="label">
    <svg class="label-shape" width="520" height="760" viewBox="0 0 520 760">
      <defs>
        <radialGradient id="medallion-gold" cx="45%" cy="40%" r="65%">
          <stop offset="0%" stop-color="#e7d2a4"/>
          <stop offset="60%" stop-color="#c5a468"/>
          <stop offset="100%" stop-color="#7d6234"/>
        </radialGradient>
      </defs>
      <rect class="label-body" x="0" y="190" width="520" height="570" fill="var(--label-black)"/>
      <circle class="label-tab" cx="260" cy="190" r="168" fill="var(--label-black)"/>
      <g class="gold-frame" fill="none" stroke="var(--gold)" stroke-width="1.5">
        <line x1="16" y1="206" x2="95" y2="206"/>
        <line x1="425" y1="206" x2="504" y2="206"/>
        <line x1="16" y1="206" x2="16" y2="744"/>
        <line x1="504" y1="206" x2="504" y2="744"/>
        <line x1="16" y1="744" x2="504" y2="744"/>
        <line x1="24" y1="214" x2="96" y2="214"/>
        <line x1="424" y1="214" x2="496" y2="214"/>
        <line x1="24" y1="214" x2="24" y2="736"/>
        <line x1="496" y1="214" x2="496" y2="736"/>
        <line x1="24" y1="736" x2="496" y2="736"/>
      </g>
      <circle class="medallion-rim" cx="260" cy="190" r="152" fill="none" stroke="var(--gold)" stroke-width="2"/>
      <circle class="medallion" cx="260" cy="190" r="146" fill="url(#medallion-gold)"
              role="img" aria-label="Round gold medallion artwork"/>
    </svg>
    <h1 class="label-text brand-name">Silvara XIV</h1>
    <p class="label-text varietals">Cabernet Sauvignon<br>Merlot • Shiraz</p>
    <p class="label-text vintage">Vintage 2023</p>
    <p class="label-text origin">New Hampshire. USA.</p>
  </section>
</main>
</body>
</html>
```